Tolvex Engineers: Why you should hire us keepsake

New design. Open to plastic cards. We are an engineering firm that designs cell phone towers and commercial buildings. Please check out our website www.tolvexgrp.com for more details. We want people to remember our card and for it to be useful if possible. We want the same look and feel on these cards to be translated to other marketing material we may need such as brochures.

Target Market(s)

Architects, Developers and Telecommunication Carriers

Industry/Entity Type

Engineering

Contact Information for Business Card

Card with our company colors, logo, and innovative design with elements related to our industry.

Font styles to use
Sans Serif

Colors
9bcb3c
abd036
0255a3

Requirements
Must have
• Sleek and hip design
Nice to have
• Bright lime green and navy coloring that pops with an innovative design.
Should not have
• A basic and boring design

```html
<!DOCTYPE html>
<html lang="en">
<head>
<meta charset="UTF-8">
<title>Tolvex Engineers – Business Card</title>
<link href="https://fonts.googleapis.com/css2?family=Montserrat:wght@400;500;800&display=swap" rel="stylesheet">
<style>
  :root {
    --navy: #0b2b5e;
    --navy-deep: #072350;
    --lime: #2cf22a;
    --white: #ffffff;
    --backdrop: #e4e5e7;
    --rule: rgba(255,255,255,0.18);
  }
  * { margin: 0; padding: 0; box-sizing: border-box; }
  html, body { width: 1200px; height: 1000px; overflow: hidden; }
  body {
    background: var(--backdrop);
    font-family: "Montserrat", Arial, sans-serif;
    position: relative;
  }
  .card {
    position: absolute;
    left: 270px;
    width: 660px;
    height: 379px;
    border-radius: 22px;
    background: linear-gradient(135deg, var(--navy) 0%, var(--navy-deep) 100%);
    box-shadow: 0 4px 10px rgba(0,0,0,0.28);
    overflow: hidden;
    color: var(--white);
  }
  .card--front { top: 108px; }
  .card--back { top: 521px; }

  .wordmark {
    font-weight: 800;
    color: var(--lime);
    letter-spacing: -2px;
    line-height: 1;
    white-space: nowrap;
  }
  .card--front .wordmark {
    position: absolute;
    top: 130px;
    left: 0; right: 0;
    text-align: center;
    font-size: 104px;
  }
  .web {
    font-size: 15px;
    font-weight: 500;
    color: var(--white);
  }
  .web .accent { color: var(--lime); }
  .card--front .web {
    position: absolute;
    top: 329px;
    left: 0; right: 0;
    text-align: center;
  }

  .card--back .wordmark {
    position: absolute;
    top: 60px;
    left: 45px;
    font-size: 80px;
  }
  .holder-name {
    position: absolute;
    top: 199px;
    left: 36px;
    font-size: 20px;
    font-weight: 400;
    color: var(--lime);
  }
  .divider {
    position: absolute;
    top: 232px;
    left: 35px;
    right: 37px;
    height: 1px;
    background: var(--rule);
  }
  .contact-list {
    position: absolute;
    top: 244px;
    left: 37px;
    list-style: none;
  }
  .contact-list li {
    display: flex;
    align-items: center;
    gap: 6px;
    font-size: 15px;
    height: 22px;
  }
  .contact-list svg { width: 11px; height: 12px; fill: var(--lime); }
  .address {
    position: absolute;
    top: 245px;
    right: 37px;
    text-align: right;
    font-size: 15px;
    line-height: 21px;
  }
  .card--back .web {
    position: absolute;
    top: 290px;
    right: 37px;
  }
  .tagline-band {
    position: absolute;
    top: 325px;
    left: 0; right: 0;
    height: 31px;
    background: var(--white);
  }
  .tagline-band .band-accent {
    position: absolute;
    left: 0; top: 0;
    width: 36px; height: 31px;
  }
  .tagline-band .tagline {
    position: absolute;
    left: 54px;
    top: 6px;
    font-size: 15px;
    color: var(--navy);
  }
</style>
</head>
<body>

  <section class="card card--front">
    <div class="wordmark">TOLVEX</div>
    <div class="web">www.<span class="accent">tolvexgrp</span>.com</div>
  </section>

  <section class="card card--back">
    <div class="wordmark">TOLVEX</div>
    <div class="holder-name">Dana Rowe Hollis</div>
    <div class="divider"></div>

    <ul class="contact-list">
      <li>
        <svg viewBox="0 0 12 12" aria-hidden="true"><path d="M2.5 0.5l2 2.3-1.2 1.3c.7 1.6 2 2.9 3.6 3.6l1.3-1.2 2.3 2-1.3 2.3C4.5 10.4 1.6 7.5.3 1.8z"/></svg>
        555.201.4410
      </li>
      <li>
        <svg viewBox="0 0 12 12" aria-hidden="true"><path d="M3 0h6a1 1 0 0 1 1 1v10a1 1 0 0 1-1 1H3a1 1 0 0 1-1-1V1a1 1 0 0 1 1-1zm.5 1.2v8h5v-8zM6 9.8a.7.7 0 1 0 0 1.4.7.7 0 0 0 0-1.4z"/></svg>
        555.318.7726
      </li>
      <li>
        <svg viewBox="0 0 12 12" aria-hidden="true"><path d="M0 2.5h12v7H0zm1 .8v.3l5 3 5-3v-.3zm0 1.5v3.9h10V4.8L6 7.8z"/></svg>
        dhollis@tolvexgrp.com
      </li>
    </ul>

    <div class="address">
      2400 Larkspur Ridge Pkwy.<br>
      Suite 310 Avondale, GA 30002
    </div>
    <div class="web">www.<span class="accent">tolvexgrp</span>.com</div>

    <div class="tagline-band">
      <svg class="band-accent" viewBox="0 0 36 31" aria-hidden="true"><polygon points="0,0 36,0 26,31 0,31" fill="#2cf22a"/></svg>
      <span class="tagline">Multi-discipline engineering</span>
    </div>
  </section>

</body>
</html>
```